Re-brand our business and design!

We need a simple informational website (editable for in the future use)
We need our logo(we have included logo), name, who we are, and what we do displayed.

This is our current site (which is not acceptable, and only a template site): all our information is on this site, please use it forreferanceofinformation.
Www.brightlanefixers.com

Target Market(s)

Real estate brokers, and realtors,homeowners, and anyone looking for home repairs.

Industry/Entity Type

Business

Number of Pages Required

4 page

Font styles to use
Sans Serif

Requirements
Must have
• Our name, contact info, services, and our logo (which we will Email upon request)
• MUST have originality to the site.
• custom "contact us form" or request an estimate form.
Nice to have
• page for real customer testimonies.
• page for our previous work where we can upload pics of completed jobs.
Should not have
• any infringements on any copyrights or plagiarism at all.

```html
<!DOCTYPE html>
<html lang="en">
<head>
<meta charset="utf-8">
<title>Bright Lane Fixers</title>
<link rel="stylesheet" href="https://fonts.googleapis.com/css2?family=Raleway:wght@300;400;500;600&family=Arimo:wght@400;700&display=swap">
<style>
:root{
  --red:#e20000;
  --ink:#2f323a;
  --card:#23252b;
  --deep:#1e2025;
  --white:#fff;
  --muted:#9a9ca2;
}
*{margin:0;padding:0;box-sizing:border-box}
html,body{width:864px;height:1200px;overflow:hidden;background:var(--ink)}
body{position:relative;font-family:'Arimo',sans-serif;color:var(--white)}
.hero{position:absolute;left:0;top:0;width:864px;height:487px;
  background:linear-gradient(90deg,#3b3b3c 0%,#5b5854 45%,#8a7d74 70%,#6b6461 100%)}
.hero-photo{position:absolute;inset:0;
  background:radial-gradient(ellipse at 72% 55%,rgba(150,70,70,.55),rgba(0,0,0,0) 45%),linear-gradient(0deg,rgba(110,100,92,.6),rgba(0,0,0,0) 40%)}
.brand{position:absolute;left:56px;top:22px;display:flex;align-items:center;gap:7px;font-family:'Raleway',sans-serif}
.brand-mark{width:12px;height:12px;background:var(--white)}
.brand-name{font-size:14px;font-weight:600}
.brand-sub{position:absolute;left:56px;top:44px;font-size:8px;font-weight:700;line-height:11px}
.nav{position:absolute;top:37px;left:0;font-family:'Raleway',sans-serif;font-size:12px}
.nav a{position:absolute;color:var(--white);text-decoration:none;white-space:nowrap}
.call{position:absolute;left:652px;top:26px;display:flex;align-items:center;gap:9px;font-family:'Raleway',sans-serif}
.call-icon{width:38px;height:38px;border-radius:50%;background:var(--white);display:flex;align-items:center;justify-content:center}
.call-label{font-size:9.5px;letter-spacing:.5px}
.call-num{font-size:16px;letter-spacing:1px}
.hero-title{position:absolute;left:57px;top:172px;font-family:'Raleway',sans-serif;font-weight:300;font-size:29px;line-height:34px}
.hero-text{position:absolute;left:57px;top:255px;width:380px;font-size:12px;line-height:18px}
.btn-touch{position:absolute;left:56px;top:316px;width:119px;height:37px;border-radius:19px;background:var(--red);font-size:11.5px;font-weight:700;display:flex;align-items:center;justify-content:center}
.services{position:absolute;left:0;top:487px;width:864px;height:391px;background:var(--ink)}
.service{position:absolute;width:240px;height:150px;background:var(--card);text-align:center}
.service svg{position:absolute;left:98px;top:28px}
.service-name{position:absolute;left:0;right:0;top:96px;font-family:'Raleway',sans-serif;font-size:15.5px;font-weight:500}
.service-name.active{color:var(--red)}
.newsletter{position:absolute;left:0;top:878px;width:864px;height:172px;background:var(--red);text-align:center}
.news-title{position:absolute;left:0;right:0;top:28px;font-family:'Raleway',sans-serif;font-weight:300;font-size:30px}
.news-sub{position:absolute;left:0;right:0;top:67px;font-size:13px}
.news-form{position:absolute;left:263px;top:104px;width:338px;height:38px;border-radius:19px;background:var(--white)}
.news-input{position:absolute;left:18px;top:12px;font-size:10.5px;color:#555}
.news-btn{position:absolute;right:1px;top:1px;width:105px;height:36px;border-radius:18px;background:var(--red);border:1px solid var(--white);font-size:12.5px;font-weight:700;display:flex;align-items:center;justify-content:center}
.footer{position:absolute;left:0;top:1050px;width:864px;height:150px;background:var(--ink)}
.legal a{position:absolute;top:33px;font-size:11px;color:var(--white);text-decoration:none}
.legal .pill{left:56px;top:23px;width:75px;height:33px;border-radius:17px;background:var(--deep);display:flex;align-items:center;justify-content:center}
.social span{position:absolute;top:23px;width:33px;height:33px;border-radius:50%}
.divider{position:absolute;left:56px;top:79px;width:753px;height:1px;background:#41444c}
.info-icon{position:absolute;top:97px;width:33px;height:33px;background:var(--deep);display:flex;align-items:center;justify-content:center}
.info{position:absolute;font-size:10.5px;line-height:17px}
.info-phone{font-size:16px;font-weight:700}
.copy{position:absolute;left:620px;top:99px;width:200px;text-align:center;font-size:10.5px;font-weight:700;line-height:17px}
.copy em{font-style:normal;font-weight:400;color:var(--red)}
</style>
</head>
<body>
<header class="hero">
  <div class="hero-photo" role="img" aria-label="Photo of a woman lying on a sofa reading a tablet on a wooden floor"></div>
  <div class="brand"><span class="brand-mark"></span><span class="brand-name">Bright Lane Fixers</span></div>
  <div class="brand-sub">And Maintenance<br>Call: 555.204.7731<br>www.brightlanefixers.com</div>
  <nav class="nav">
    <a style="left:282px">Home</a>
    <a style="left:361px">About</a>
    <a style="left:441px">Services</a>
    <a style="left:534px">Contact</a>
  </nav>
  <div class="call">
    <div class="call-icon"><svg width="18" height="18" viewBox="0 0 24 24" fill="none" stroke="#333" stroke-width="1.4"><path d="M5 3h4l2 5-3 2a12 12 0 0 0 6 6l2-3 5 2v4a2 2 0 0 1-2 2A17 17 0 0 1 3 5a2 2 0 0 1 2-2z"/></svg></div>
    <div><div class="call-label">CALL US ON</div><div class="call-num">555.204.7731</div></div>
  </div>
  <h1 class="hero-title">Looking for someone to help<br>get your listing ready to show?</h1>
  <p class="hero-text">A complete Home Repair Solution? Did an inspection reveal repairs needed before closing? Bright Lane Fixers can help!</p>
  <div class="btn-touch">GET IN TOUCH</div>
</header>

<section class="services">
  <div class="service" style="left:55px;top:38px">
    <svg width="44" height="44" viewBox="0 0 44 44" fill="none" stroke="#fff" stroke-width="1.5"><path d="M4 4l30 30 4-4L8 2z"/><path d="M32 30l6 6 3-3-6-6"/></svg>
    <div class="service-name active">CARPENTRY</div>
  </div>
  <div class="service" style="left:312px;top:38px">
    <svg width="44" height="44" viewBox="0 0 44 44" fill="none" stroke="#e20000" stroke-width="1.5"><path d="M2 4h10v8h14v14h-6v-8H2z"/><path d="M36 32c-2 3-3 5-3 6a3 3 0 0 0 6 0c0-1-1-3-3-6z" transform="translate(-13 0)"/></svg>
    <div class="service-name">PLUMBING</div>
  </div>
  <div class="service" style="left:568px;top:38px">
    <svg width="48" height="44" viewBox="0 0 48 44" fill="none" stroke="#e20000" stroke-width="1.5"><rect x="16" y="2" width="28" height="40"/><path d="M20 6h20v30H20zM30 6v30M20 21h20"/><path d="M16 4L4 10v28l12 4"/></svg>
    <div class="service-name">DOORS &amp; WINDOWS</div>
  </div>
  <div class="service" style="left:55px;top:203px">
    <svg width="44" height="44" viewBox="0 0 44 44" fill="none" stroke="#e20000" stroke-width="1.5"><path d="M24 2L10 26h10l-4 16 16-24H22z"/></svg>
    <div class="service-name">ELECTRICAL</div>
  </div>
  <div class="service" style="left:312px;top:203px">
    <svg width="44" height="44" viewBox="0 0 44 44" fill="none" stroke="#e20000" stroke-width="1.5"><path d="M6 20a16 16 0 0 1 32 0z"/><path d="M18 5v12M26 5v12M3 20h38v4H3z"/><path d="M8 24c2 10 8 16 14 16s12-6 14-16"/></svg>
    <div class="service-name">SMALL CONSTRUCTION</div>
  </div>
  <div class="service" style="left:568px;top:203px">
    <svg width="64" height="44" viewBox="0 0 64 44" fill="none" stroke="#e20000" stroke-width="1.8" style="left:88px"><path d="M10 4h44l8 38H2z"/><path d="M4 16h56M3 28h58M21 4l-4 38M32 4v38M43 4l4 38"/></svg>
    <div class="service-name">ROOFING MAINTENANCE</div>
  </div>
</section>

<section class="newsletter">
  <h2 class="news-title">Newsletter</h2>
  <p class="news-sub">Be first in line. Get notified when we go live.</p>
  <div class="news-form">
    <span class="news-input">Your E-mail Address</span>
    <div class="news-btn">SUBSCRIBE</div>
  </div>
</section>

<footer class="footer">
  <nav class="legal">
    <a class="pill">COOKIES</a>
    <a style="left:152px">PRIVACY POLICY</a>
    <a style="left:266px">DISCLAIMER</a>
  </nav>
  <div class="social">
    <span style="left:692px;background:var(--deep)"></span>
    <span style="left:734px;background:#6b6d73"></span>
    <span style="left:776px;background:#6b6d73"></span>
  </div>
  <div class="divider"></div>
  <div class="info-icon" style="left:56px"><svg width="16" height="18" viewBox="0 0 16 18" fill="none" stroke="#fff" stroke-width="1.2"><path d="M8 17s6-6 6-10A6 6 0 0 0 2 7c0 4 6 10 6 10z"/><circle cx="8" cy="7" r="2"/></svg></div>
  <div class="info" style="left:99px;top:99px">123&nbsp;&nbsp;&nbsp;&nbsp;Building Name, Street,<br>City, Country - Zipcode</div>
  <div class="info-icon" style="left:247px"><svg width="16" height="16" viewBox="0 0 24 24" fill="none" stroke="#fff" stroke-width="1.4"><path d="M5 3h4l2 5-3 2a12 12 0 0 0 6 6l2-3 5 2v4a2 2 0 0 1-2 2A17 17 0 0 1 3 5a2 2 0 0 1 2-2z"/></svg></div>
  <div class="info info-phone" style="left:290px;top:103px">555-204-7731</div>
  <div class="info-icon" style="left:437px"><svg width="18" height="14" viewBox="0 0 18 14" fill="none" stroke="#fff" stroke-width="1.2"><rect x="1" y="1" width="16" height="12"/><path d="M1 1l8 7 8-7M1 13l6-6M17 13l-6-6"/></svg></div>
  <div class="info" style="left:480px;top:106px">mark@brightlanefixers.com</div>
  <div class="copy">© <em>Bright Lane Fixers</em> - 2016.<br>All Rights Reserved.</div>
</footer>
</body>
</html>
```